Software company seeking fresh website design

Using an already existing logo create a fresh, clean and professional web design for our company "Nimbra Works". Nimbra Works focuses on making business better through system integrations and software product development.

We're looking for a web design which has layouts for the following pages:
- Home Page
- Team Page
- Case Studies
- Market (List of Products)
- Product Page (Individual Product Details)
- About Page
- Media Page

Some websites and designs we'd like you to take inspiration from:
- Quarnel.com
- https://www.plorvate.net/gallery/71830264/Vantrel-redesign
- https://zimmerpost.com/shots/5918304-Bright-Frames-Website-Design-for-a-Software-Company

Ideally the design should communicate an enterprise-level business with years of experience that can be trusted to deliver on budget and on-time.

Target Market(s)

Medium to High-Level Enterprise

Industry/Entity Type

Software Development

Coding

Coded - Design and coding required

Number of Pages Required

5+ page

Font styles to use
Sans Serif

Colors

Designer to choose colors to be used in the design.

Requirements
Must have
• - High Level of Professionalism
• - Be a unique design
• - Come with well-formatted and organised html + css + javascript
• - Must work on ie9, latest Chrome, latest Firefox, latest safari. iPhone6 and Android
• - Must be a progressive template
• - Must incorporate logo colors or at least be compatible with them
Nice to have
• - Hero, an area to display things we're proud of but look good without that area if need be.
• - Juicy animations that are performant and degrade nicely
Should not have
• - Submission must not be a template re-branded for the business

```html
<!DOCTYPE html>
<html lang="en">
<head>
<meta charset="utf-8">
<title>Nimbra Works</title>
<link href="https://fonts.googleapis.com/css2?family=Jost:wght@400;500;600;700&display=swap" rel="stylesheet">
<style>
:root{
  --orange:#f26522;
  --orange-light:#f7931e;
  --ink:#111111;
  --text:#555a66;
  --navy:#1e2046;
  --white:#ffffff;
  --line:#ececec;
}
*{box-sizing:border-box;margin:0;padding:0}
html,body{width:1200px;height:3303px;overflow:hidden}
body{font-family:"Jost",Arial,sans-serif;background:var(--white);color:var(--ink);position:relative}
.abs{position:absolute}
.btn{position:absolute;display:flex;align-items:center;justify-content:center;font-size:11px;font-weight:600;letter-spacing:.5px;text-transform:uppercase;border-radius:4px}
.btn-dark{background:var(--ink);color:var(--white)}
.btn-orange{background:var(--orange);color:var(--white)}

/* header */
.site-header{position:absolute;left:0;top:0;width:1200px;height:84px;border-bottom:1px solid var(--line)}
.brand{position:absolute;display:flex;align-items:center;gap:8px;font-weight:600;white-space:nowrap}
.brand-mark{width:22px;height:22px;background:var(--orange);border-radius:4px}
.header-brand{left:160px;top:29px;color:var(--ink);font-size:19px}
.main-nav a{position:absolute;top:35px;font-size:12px;color:var(--ink);text-decoration:none;white-space:nowrap}
.btn-login{left:821px;top:26px;width:104px;height:36px;border:1.5px solid var(--orange);color:var(--orange);text-transform:none;font-size:12px}
.btn-signup{left:936px;top:26px;width:101px;height:36px;text-transform:none;font-size:12px}

/* hero */
.hero-band{position:absolute;background:var(--orange)}
.hero-card{position:absolute;left:160px;top:137px;width:877px;height:451px;background:linear-gradient(135deg,#f2661f,#f47b2a);border-radius:4px;box-shadow:0 6px 20px rgba(0,0,0,.12)}
.hero-title{position:absolute;left:32px;top:36px;color:var(--white);font-size:42px;font-weight:600;line-height:1.18}
.hero-sub{position:absolute;left:32px;top:170px;color:var(--white);font-size:14px;font-weight:500}
.hero-card .btn{left:32px;top:233px;width:169px;height:42px}
.hero-dots{position:absolute;left:250px;top:198px;width:603px;height:228px;border-radius:6px;background:linear-gradient(90deg,rgba(255,255,255,.35),rgba(255,255,255,.22))}

/* products */
.section-title{position:absolute;left:0;width:1200px;text-align:center;color:var(--orange);font-size:44px;font-weight:600}
.product-icon{position:absolute;width:126px;height:95px;background:var(--orange);border-radius:3px;display:flex;align-items:center;justify-content:center}
.product-name{position:absolute;color:var(--orange);font-size:14px;font-weight:600}
.product-desc{position:absolute;width:250px;font-size:11px;line-height:1.55;color:var(--text)}
.divider{position:absolute;left:0;width:1200px;height:1px;background:var(--line)}

/* tools */
.tool-tile{position:absolute;width:206px;height:77px;background:var(--white);border-radius:4px;box-shadow:0 2px 10px rgba(0,0,0,.12);display:flex;align-items:center;justify-content:center;font-size:26px;font-weight:500;color:#2a2a2a}
.tools-title{position:absolute;left:680px;top:1086px;color:var(--orange);font-size:44px;font-weight:600;line-height:1.25}
.tools-text{position:absolute;left:680px;top:1220px;font-size:12px;color:var(--text)}

/* case studies */
.case-heading{position:absolute;left:160px;top:1516px;color:var(--white);font-size:36px;font-weight:600}
.case-intro{position:absolute;left:160px;top:1576px;width:410px;color:var(--white);font-size:11px;font-weight:500;line-height:1.55}
.case-sub{position:absolute;left:680px;top:1522px;color:var(--white);font-size:20px;font-weight:500}
.case-item{position:absolute;left:600px;width:440px;height:100px;color:var(--white)}
.case-avatar{position:absolute;left:0;top:0;width:68px;height:68px;border-radius:50%;background:rgba(255,255,255,.28);display:flex;align-items:center;justify-content:center}
.case-quote{position:absolute;left:88px;top:0;font-size:38px;font-weight:700;line-height:1}
.case-date{position:absolute;left:80px;top:40px;width:54px;text-align:center;font-size:10px;font-weight:600;line-height:1.5}
.case-label{position:absolute;left:140px;top:4px;font-size:12px;font-weight:600}
.case-body{position:absolute;left:140px;top:24px;width:300px;font-size:10.5px;line-height:1.6}

/* team */
.team-card{position:absolute;top:2145px;width:243px}
.team-photo{width:243px;height:273px;background:linear-gradient(180deg,#f4f4f4,#d9dde2);box-shadow:0 2px 10px rgba(0,0,0,.12)}
.team-name{margin-top:22px;text-align:center;font-size:14px;font-weight:600}
.team-bio{margin-top:8px;text-align:center;font-size:11px;line-height:1.55;color:var(--text)}

/* cta + footer */
.site-footer{position:absolute;left:0;top:2633px;width:1200px;height:670px;background:var(--navy);color:var(--white)}
.cta-title{position:absolute;left:160px;top:116px;font-size:42px;font-weight:600;line-height:1.3}
.cta-text{position:absolute;left:160px;top:236px;font-size:11px;color:#6d7196}
.cta-btn{left:867px;top:154px;width:170px;height:45px}
.footer-rule{position:absolute;left:160px;top:351px;width:877px;height:1px;background:#34376a}
.footer-brand{left:160px;top:400px;color:var(--white);font-size:22px}
.footer-small{position:absolute;font-size:11px;color:#8a8eb3}
.footer-head{position:absolute;top:404px;font-size:11px;font-weight:600;letter-spacing:.5px;text-transform:uppercase}
.contact-line{position:absolute;left:506px;display:flex;gap:12px;font-size:11px;color:#b9bcd8;line-height:1.6}
.footer-nav a{position:absolute;left:878px;font-size:11px;color:#8a8eb3;text-decoration:none}
.social{position:absolute;top:544px;width:12px;height:12px;background:#6d7196;border-radius:2px}
</style>
</head>
<body>

<header class="site-header">
  <div class="brand header-brand"><span class="brand-mark"></span>Nimbra Works</div>
  <nav class="main-nav">
    <a style="left:363px">Home</a>
    <a style="left:432px">Case Studies</a>
    <a style="left:533px">Market</a>
    <a style="left:608px">Products</a>
    <a style="left:689px">About</a>
    <a style="left:757px">Team</a>
  </nav>
  <a class="btn btn-login">Login</a>
  <a class="btn btn-orange btn-signup">Sign Up</a>
</header>

<section class="hero">
  <div class="hero-band" style="left:0;top:429px;width:170px;height:66px"></div>
  <div class="hero-band" style="left:1030px;top:293px;width:170px;height:70px"></div>
  <svg class="abs" style="left:810px;top:580px" width="80" height="62" viewBox="0 0 80 62"><path d="M10 0 H70 C60 20 50 45 72 60 C40 55 20 35 10 0 Z" fill="#f26522"/></svg>
  <div class="hero-card">
    <h1 class="hero-title">Accelerating Enterprise<br>Innovation</h1>
    <p class="hero-sub">Through proven strategic initiatives.</p>
    <a class="btn btn-dark">Learn More</a>
    <div class="hero-dots" role="img" aria-label="Grid of soft light dots in varying brightness"></div>
  </div>
</section>

<section class="products">
  <h2 class="section-title" style="top:662px">Our Products</h2>
  <div class="product-icon" style="left:160px;top:775px">
    <svg width="56" height="56" viewBox="0 0 56 56" fill="none" stroke="#fff" stroke-width="2.5"><path d="M28 14a12 12 0 0 0-7 22v6h14v-6a12 12 0 0 0-7-22z"/><path d="M22 47h12M28 4v4M10 12l3 3M46 12l-3 3M4 28h4M48 28h4"/></svg>
  </div>
  <div class="product-name" style="left:313px;top:772px">Pollen Note</div>
  <p class="product-desc" style="left:313px;top:804px">Pollen Note is a simple script which you put into your web page or web application which helps your customers to give you feedback about bugs</p>
  <div class="product-icon" style="left:645px;top:775px">
    <svg width="60" height="56" viewBox="0 0 60 56" fill="none" stroke="#fff" stroke-width="2.5"><rect x="6" y="10" width="40" height="28" rx="2"/><path d="M2 44h48M36 30l10 10M50 20a6 6 0 1 1-8 8"/></svg>
  </div>
  <div class="product-name" style="left:793px;top:772px">quillet.io</div>
  <p class="product-desc" style="left:793px;top:804px">Quillet is a simple one-way anonymous email relay. It allows you to do simple things like sign up for downloads and not have to worry about</p>
  <div class="divider" style="top:951px"></div>
</section>

<section class="tools">
  <div class="tool-tile" style="left:160px;top:1068px">Orbel</div>
  <div class="tool-tile" style="left:381px;top:1068px">Harbix</div>
  <div class="tool-tile" style="left:160px;top:1160px">Selvadb</div>
  <div class="tool-tile" style="left:381px;top:1160px">Tundrix</div>
  <div class="tool-tile" style="left:160px;top:1253px">Corvo</div>
  <div class="tool-tile" style="left:381px;top:1253px">Quenby</div>
  <h2 class="tools-title">Tools Of Our<br>Trade</h2>
  <p class="tools-text">Nimbra Works build scalable Apps for any sized client. Our skills include:</p>
  <a class="btn btn-dark" style="left:680px;top:1270px;width:172px;height:46px">Learn More</a>
</section>

<section class="case-studies">
  <svg class="abs" style="left:0;top:1442px" width="1200" height="652" viewBox="0 1442 1200 652">
    <defs><linearGradient id="caseGrad" x1="0" x2="1"><stop offset="0" stop-color="#f05a22"/><stop offset="1" stop-color="#f7931e"/></linearGradient></defs>
    <path d="M0 1442 H1200 V2092 C1060 2010 900 1950 730 1945 C520 1940 420 1925 330 1875 C210 1805 120 1700 0 1625 Z" fill="url(#caseGrad)"/>
  </svg>
  <h2 class="case-heading">Case Studies</h2>
  <p class="case-intro">The following are snapshot of some of the work we've done for clients. By default, all our clients are held confidential so names displayed here are done so only with the explicit permission of the business.</p>
  <a class="btn btn-dark" style="left:160px;top:1658px;width:173px;height:44px">Learn More</a>
  <h3 class="case-sub">Self-Help &amp; Wellness</h3>

  <div class="case-item" style="top:1574px">
    <div class="case-avatar"><svg width="30" height="30" viewBox="0 0 30 30" fill="none" stroke="#fff" stroke-width="2"><circle cx="15" cy="10" r="6"/><path d="M4 28c0-6 5-10 11-10s11 4 11 10z"/></svg></div>
    <div class="case-quote">“</div>
    <div class="case-date">August 10, 2016</div>
    <div class="case-label">The Business</div>
    <p class="case-body">Our clients are a Self-Help &amp; Wellness internet marketing company ranked in the top 200 for the Religion &amp; Spirituality category. With hundreds of products, thousands of</p>
  </div>
  <div class="case-item" style="top:1692px">
    <div class="case-avatar"><svg width="30" height="30" viewBox="0 0 30 30" fill="none" stroke="#fff" stroke-width="2"><circle cx="15" cy="10" r="6"/><path d="M4 28c0-6 5-10 11-10s11 4 11 10z"/></svg></div>
    <div class="case-quote">“</div>
    <div class="case-date">August 10, 2016</div>
    <div class="case-label">The Problem</div>
    <p class="case-body">After a year-on-year reduction of profits, the business was seeking a way to innovate and re-engage customers with their product line and brand.</p>
  </div>
  <div class="case-item" style="top:1808px">
    <div class="case-avatar"><svg width="30" height="30" viewBox="0 0 30 30" fill="none" stroke="#fff" stroke-width="2"><circle cx="15" cy="10" r="6"/><path d="M4 28c0-6 5-10 11-10s11 4 11 10z"/></svg></div>
    <div class="case-quote">“</div>
    <div class="case-date">August 10, 2016</div>
    <div class="case-label">Services Rendered</div>
    <p class="case-body">1. Stakeholder Engagement &nbsp; 2. Site Scalability &amp; Sustainability Testing &nbsp; 3. Lean Customer Validation &nbsp; 4. MVP Development</p>
  </div>
</section>

<section class="team">
  <h2 class="section-title" style="top:2052px">Our Team</h2>
  <div class="team-card" style="left:160px">
    <div class="team-photo" role="img" aria-label="Portrait of a smiling team member in a grey shirt, arms crossed"></div>
    <div class="team-name">Owen Farley</div>
    <p class="team-bio">Lorem ipsum dolor sit amet, consectetur adipiscing elit, sed do eiusmod tempor.</p>
  </div>
  <div class="team-card" style="left:478px">
    <div class="team-photo" role="img" aria-label="Portrait of a smiling team member in shirt and tie, arms crossed"></div>
    <div class="team-name">Reuben Castell</div>
    <p class="team-bio">Lorem ipsum dolor sit amet, consectetur adipiscing elit, sed do eiusmod tempor.</p>
  </div>
  <div class="team-card" style="left:793px">
    <div class="team-photo" role="img" aria-label="Portrait of a smiling team member in a grey cardigan, arms crossed"></div>
    <div class="team-name">Ilse Moreton</div>
    <p class="team-bio">Lorem ipsum dolor sit amet, consectetur adipiscing elit, sed do eiusmod tempor.</p>
  </div>
</section>

<footer class="site-footer">
  <h2 class="cta-title">Make your business<br>with Nimbra Works</h2>
  <p class="cta-text">Accelerating Enterprise Innovation Through proven strategic initiatives.</p>
  <a class="btn btn-orange cta-btn">Learn More</a>
  <div class="footer-rule"></div>

  <div class="brand footer-brand"><span class="brand-mark"></span>Nimbra Works</div>
  <div class="footer-small" style="left:160px;top:498px">hello@nimbraworks.co</div>
  <span class="social" style="left:160px"></span>
  <span class="social" style="left:190px"></span>
  <span class="social" style="left:220px"></span>
  <span class="social" style="left:250px"></span>
  <div class="footer-small" style="left:160px;top:576px;font-size:10px">© Copyright 2018 Nimbra Works co., All Rights Reserved</div>

  <div class="footer-head" style="left:506px">Contact Us</div>
  <div class="contact-line" style="top:440px"><svg width="12" height="14" viewBox="0 0 12 14"><path d="M6 0a5 5 0 0 0-5 5c0 4 5 9 5 9s5-5 5-9a5 5 0 0 0-5-5z" fill="#8a8eb3"/><circle cx="6" cy="5" r="2" fill="#1e2046"/></svg><span>27 Kestrel Lane, Marlow Heights Queensland,<br>Australia 4410</span></div>
  <div class="contact-line" style="top:492px"><svg width="12" height="12" viewBox="0 0 12 12"><path d="M2 0h3l1 3-2 1a7 7 0 0 0 4 4l1-2 3 1v3a1 1 0 0 1-1 1A11 11 0 0 1 1 1a1 1 0 0 1 1-1z" fill="#8a8eb3"/></svg><span>(+614) 5550 1847</span></div>
  <div class="contact-line" style="top:522px;color:#fff"><svg width="13" height="10" viewBox="0 0 13 10"><rect width="13" height="10" rx="1" fill="#fff"/><path d="M1 1l5.5 4L12 1" stroke="#1e2046" fill="none"/></svg><span>hello@nimbraworks.co</span></div>

  <div class="footer-head" style="left:878px">Navigation</div>
  <nav class="footer-nav">
    <a style="top:440px">Home</a>
    <a style="top:466px">Case Studies</a>
    <a style="top:492px">Market</a>
    <a style="top:518px">Products</a>
    <a style="top:544px">About</a>
    <a style="top:570px">Team</a>
  </nav>
</footer>

</body>
</html>
```